The Christian Teacher Life-Cycle

Look at the Lifecyle of the Christian School.
Look at the Calloway Brook logo.
I am looking for a Christian Teacher Lifecycle that represents the slides in the PP upload.
Our website is callowaybrookguidance.org.
The design should include a summary design showing all four stages, and then four slides representing each of the stages as subsets of the summary design.
When a teacher is going through the Lifecycle, they are going on their Professional Learning Journey that takes 40 years to unfold.
All five should include a copyright 2026 Calloway Brook on them.

```html
<!DOCTYPE html>
<html lang="en">
<head>
<meta charset="utf-8">
<title>Calloway Brook – Mission Delivery Slides</title>
<link rel="stylesheet" href="https://fonts.googleapis.com/css2?family=Marcellus&family=Pinyon+Script&family=Jost:wght@400;500;600&display=swap">
<style>
:root{
  --blue:#1570ad;
  --blue-soft:#5f9ac7;
  --ink:#222222;
  --grey:#6e7176;
  --paper:#f7f6f2;
  --sky-1:#eef4fa;
  --sky-2:#dde9f5;
  --white:#ffffff;
}
*{margin:0;padding:0;box-sizing:border-box}
html,body{width:1006px;height:1200px;overflow:hidden;background:var(--white)}
body{position:relative;font-family:"Jost",sans-serif;color:var(--ink)}
.slide{position:absolute;width:456px;height:256px;overflow:hidden;
  background:linear-gradient(160deg,var(--sky-1),var(--sky-2) 55%,var(--sky-1));
  box-shadow:0 3px 6px rgba(0,0,0,.18)}
.slide.plain{background:var(--white)}
.slide.paper{background:var(--paper)}
.abs{position:absolute}
.brand-name{position:absolute;left:14px;top:34px;font-family:"Jost",sans-serif;font-weight:500;font-size:13px;color:var(--blue);line-height:1;white-space:nowrap}
.motto{position:absolute;left:14px;top:60px;font-size:5px;color:var(--grey)}
.motto::before{content:"";display:inline-block;width:4px;height:4px;background:var(--blue-soft);transform:rotate(45deg);margin-right:3px;vertical-align:middle}
.footer{position:absolute;left:13px;top:218px;font-size:6.1px;line-height:8.4px;color:var(--ink)}
.footer b{font-weight:600}
.page{position:absolute;right:14px;top:234px;font-family:"Marcellus",serif;font-size:8.5px}
.tag{position:absolute;background:var(--blue);color:var(--white);font-family:"Marcellus",serif;
  display:flex;align-items:center;justify-content:center;white-space:nowrap}
.heading{position:absolute;font-family:"Marcellus",serif;color:var(--ink);white-space:nowrap;line-height:1}
.step-tag{left:14px;width:97px;height:16px;font-size:10px}
.step-title{left:20px;font-size:21px}
.card{position:absolute;background:var(--white);border:1px solid #d8e2ec;border-radius:6px;padding:6px 7px;font-size:6.4px;line-height:8.2px}
.card ul{list-style:none}
.card li{margin-bottom:3.6px}
.card li::before{content:"• "}
.placeholder{position:absolute}
.note{position:absolute;background:#fbfbfa;box-shadow:0 1px 3px rgba(0,0,0,.15);padding:14px 8px 6px;font-size:6.3px;line-height:8px}
.note::before{content:"";position:absolute;left:6px;right:6px;top:4px;height:5px;
  background:radial-gradient(circle,#c9cdd2 1.4px,transparent 1.8px) 0 0/13px 5px repeat-x}
.note li{list-style:none;margin-bottom:4px}
.note li::before{content:"• "}
.note-tag{height:13px;font-size:7px;border-radius:2px}
.stage-label{position:absolute;padding-left:4px;border-left:1px solid #8a8a8a;font-size:5.6px;line-height:7.6px;color:var(--ink)}
.stage-label .name{font-family:"Marcellus",serif;color:var(--blue);font-size:7.2px;line-height:7.4px;margin-bottom:3px}
.cloud{position:absolute}
.cloud-text{position:absolute;inset:0;display:flex;flex-direction:column;align-items:center;justify-content:center;text-align:center;font-size:5.4px;line-height:6.4px;color:var(--grey);padding:8px 18px 0}
.cloud-text b{color:var(--ink);font-weight:500;font-size:6px;margin-bottom:5px}
</style>
</head>
<body>

<svg width="0" height="0" style="position:absolute">
  <defs>
    <path id="cloud-shape" d="M22 62 C6 62 3 44 16 38 C11 22 30 12 42 20 C48 4 78 4 82 20 C98 13 112 28 102 40 C115 46 110 64 94 62 Z"/>
  </defs>
</svg>

<!-- Slide 1: title -->
<section class="slide plain" style="left:27px;top:24px">
  <svg class="abs" width="456" height="256" viewBox="0 0 456 256" style="left:0;top:0">
    <defs>
      <linearGradient id="glass" x1="0" y1="0" x2="1" y2="1">
        <stop offset="0" stop-color="#0b0b0b"/>
        <stop offset=".45" stop-color="#6b4a18"/>
        <stop offset=".7" stop-color="#8a2a1e"/>
        <stop offset="1" stop-color="#1a1a1a"/>
      </linearGradient>
    </defs>
    <path d="M190 0 C232 60 230 170 178 256 L186 256 C238 170 240 60 200 0 Z" fill="var(--blue)"/>
    <path d="M200 0 L456 0 L456 256 L186 256 C238 170 240 60 200 0 Z" fill="url(#glass)" role="img" aria-label="Stained glass arched church window with light rays"/>
  </svg>
  <div class="brand-name">Calloway Brook</div>
  <div class="motto">For Jesus; Through Mission; With Children</div>
  <div class="heading" style="left:14px;top:92px;font-family:'Pinyon Script',cursive;font-size:38px">For Jesus;</div>
  <div class="heading" style="left:14px;top:136px;font-size:20px">Through Mission;</div>
  <div class="tag" style="left:13px;top:165px;width:154px;height:19px;font-family:'Jost',sans-serif;font-size:8.5px;letter-spacing:2px;font-style:italic">With Children</div>
  <div class="footer"><b>Mission Delivery</b><br>©2026 Calloway Brook Guidance - Principal<br>Certification Poimen: Shepherd</div>
  <div class="page" style="color:var(--white)">1</div>
</section>

<!-- Slide 2: school lifecycle -->
<section class="slide paper" style="left:516px;top:24px">
  <div class="brand-name">Calloway Brook</div>
  <div class="motto">For Jesus; Through Mission; With Children</div>
  <div class="tag" style="left:190px;top:10px;width:144px;height:19px;font-size:11px">Calloway Brook Christian</div>
  <div class="heading" style="left:208px;top:32px;font-size:15px">School Lifecycle</div>
  <svg class="abs" width="456" height="256" viewBox="0 0 456 256" style="left:0;top:0" role="img" aria-label="Illustration of four trees growing on a brown hill, from sapling to bare dying tree">
    <defs>
      <linearGradient id="hill" x1="0" y1="0" x2="0" y2="1">
        <stop offset="0" stop-color="#9b7a2e"/>
        <stop offset="1" stop-color="#b07a22"/>
      </linearGradient>
    </defs>
    <path d="M54 210 C120 196 170 168 230 160 C280 152 330 160 380 186 C400 196 418 206 430 210 Z" fill="url(#hill)"/>
    <line x1="40" y1="210" x2="436" y2="210" stroke="#8a8a8a" stroke-width=".6"/>
  </svg>
  <div class="stage-label" style="left:75px;top:121px"><div class="name">The Enthusiastic<br>Christian School</div>(entrepreneurial)<br>0-10 years</div>
  <div class="stage-label" style="left:149px;top:92px"><div class="name">The Confident<br>Christian School</div>(adolescent)<br>10-15 years</div>
  <div class="stage-label" style="left:220px;top:63px"><div class="name">The Inspired<br>Christian School</div>(mature)<br>15-30+ years</div>
  <div class="stage-label" style="left:314px;top:94px"><div class="name">The Proud<br>Christian School</div>(dying)<br>20+ years</div>
  <div class="footer"><b>Mission Delivery</b><br>©2026 Calloway Brook Guidance - Principal<br>Certification Poimen: Shepherd</div>
  <div class="page">2</div>
</section>

<!-- Slide 3: stages of growth -->
<section class="slide" style="left:27px;top:317px">
  <div class="brand-name">Calloway Brook</div>
  <div class="motto">For Jesus; Through Mission; With Children</div>
  <div class="tag" style="left:154px;top:17px;width:214px;height:19px;font-size:13.5px">Professional Learning Journey</div>
  <div class="heading" style="left:205px;top:40px;font-size:14px">Stages of Growth</div>

  <div class="cloud" style="left:48px;top:118px;width:118px;height:70px">
    <svg width="118" height="70" viewBox="-2 0 118 70"><use href="#cloud-shape" fill="none" stroke="var(--blue-soft)" stroke-width=".8" stroke-dasharray="3 2" transform="translate(57 34) scale(1.08) translate(-57 -34)"/><use href="#cloud-shape" fill="var(--white)" stroke="var(--blue)" stroke-width="1.2"/></svg>
    <div class="cloud-text"><b>Stage 01</b>The focus is<br>on “I”</div>
  </div>
  <div class="cloud" style="left:140px;top:68px;width:118px;height:70px">
    <svg width="118" height="70" viewBox="-2 0 118 70"><use href="#cloud-shape" fill="none" stroke="var(--blue-soft)" stroke-width=".8" stroke-dasharray="3 2" transform="translate(57 34) scale(1.08) translate(-57 -34)"/><use href="#cloud-shape" fill="var(--white)" stroke="var(--blue)" stroke-width="1.2"/></svg>
    <div class="cloud-text"><b>Stage 02</b>Becoming part of the Christian Professional Learning Community</div>
  </div>
  <div class="cloud" style="left:224px;top:130px;width:118px;height:70px">
    <svg width="118" height="70" viewBox="-2 0 118 70"><use href="#cloud-shape" fill="none" stroke="var(--blue-soft)" stroke-width=".8" stroke-dasharray="3 2" transform="translate(57 34) scale(1.08) translate(-57 -34)"/><use href="#cloud-shape" fill="var(--white)" stroke="var(--blue)" stroke-width="1.2"/></svg>
    <div class="cloud-text"><b>Stage 03</b>Learning leadership within the faculty culture / CPLC</div>
  </div>
  <div class="cloud" style="left:294px;top:66px;width:118px;height:70px">
    <svg width="118" height="70" viewBox="-2 0 118 70"><use href="#cloud-shape" fill="none" stroke="var(--blue-soft)" stroke-width=".8" stroke-dasharray="3 2" transform="translate(57 34) scale(1.08) translate(-57 -34)"/><use href="#cloud-shape" fill="var(--white)" stroke="var(--blue)" stroke-width="1.2"/></svg>
    <div class="cloud-text"><b>Stage 04</b>So good, I am “invisible”; I have let go of control and share it with my children/teens</div>
  </div>

  <div class="abs" style="left:207px;top:213px;width:221px;height:35px;background:var(--white);border:1px solid #8a8a8a;padding:5px 7px;font-size:4.5px;line-height:6.6px">All are good. The only sin is not growing. It is a 40 year career-long Professional Learning Journey. I want to grow so that children and teenagers will become more than before. They are also on a life-long Personal Learning Journey.</div>
  <div class="footer"><b>Mission Delivery</b><br>©2026 Calloway Brook Guidance - Principal<br>Certification Poimen: Shepherd</div>
  <div class="page">3</div>
</section>

<!-- Slide 4: step one -->
<section class="slide" style="left:516px;top:317px">
  <div class="brand-name">Calloway Brook</div>
  <div class="motto">For Jesus; Through Mission; With Children</div>
  <div class="tag step-tag" style="top:81px">Learning Journey</div>
  <div class="heading step-title" style="top:98px">Step One</div>
  <div class="card" style="left:12px;top:126px;width:204px;height:80px">
    <ul>
      <li>The focus is on “I”</li>
      <li>Fundamental skills dominate such as classroom management.</li>
      <li>Curriculum is where I spend my time.</li>
      <li>I am a sponge rather than a contributor.</li>
      <li>I see myself as a learner.</li>
      <li>I reflect on my practice.</li>
    </ul>
  </div>
  <div class="placeholder" role="img" aria-label="Photo of a young girl in denim sitting thoughtfully on grass, in a scalloped blue frame"
       style="left:237px;top:37px;width:187px;height:189px;border:2.5px solid var(--blue);border-radius:22px;background:linear-gradient(160deg,#6f8f4a,#3f6ea0 60%,#2c4f78)"></div>
  <div class="footer"><b>Mission Delivery</b><br>©2026 Calloway Brook Guidance - Principal<br>Certification Poimen: Shepherd</div>
  <div class="page">4</div>
</section>

<!-- Slide 5: step two -->
<section class="slide" style="left:27px;top:610px">
  <div class="brand-name">Calloway Brook</div>
  <div class="motto">For Jesus; Through Mission; With Children</div>
  <div class="tag step-tag" style="top:80px">Learning Journey</div>
  <div class="heading step-title" style="top:97px">Step Two</div>
  <div class="card" style="left:14px;top:127px;width:216px;height:80px">
    <ul>
      <li>My Christian Professional Learning Community is important to me as a place where I give and take.</li>
      <li>I recognize that “we” is more powerful for the child than “I”</li>
      <li>I know my curriculum - I am more focused on how, on pedagogy.</li>
      <li>I assess relevant and effective assessment tools.</li>
      <li>I reflect on my practice.</li>
    </ul>
  </div>
  <div class="placeholder" role="img" aria-label="Cartoon illustration of two children reading a green book together"
       style="left:262px;top:48px;width:150px;height:158px;border-radius:12px;background:linear-gradient(170deg,#f3d2b0 0%,#e8a870 45%,#5cc0a0 80%,#eaf2f8 100%)"></div>
  <div class="footer"><b>Mission Delivery</b><br>©2026 Calloway Brook Guidance - Principal<br>Certification Poimen: Shepherd</div>
  <div class="page">5</div>
</section>

<!-- Slide 6: step three -->
<section class="slide" style="left:516px;top:610px">
  <div class="brand-name">Calloway Brook</div>
  <div class="motto">For Jesus; Through Mission; With Children</div>
  <div class="tag step-tag" style="top:118px">Learning Journey</div>
  <div class="heading step-title" style="left:13px;top:135px">Step Three</div>
  <div class="tag note-tag" style="left:192px;top:14px;width:58px">Step Three (A)</div>
  <div class="note" style="left:149px;top:33px;width:148px;height:126px">
    <ul>
      <li>I lead in my Christian Professional Learning Community.</li>
      <li>Ensuring my colleagues continue to grow is critical to me.</li>
      <li>Together, we are humble in understanding where we still need to go.</li>
      <li>My colleagues see me as an important resource.</li>
      <li>I am a master of growth.</li>
      <li>I help my colleagues reflect.</li>
    </ul>
  </div>
  <div class="tag note-tag" style="left:324px;top:97px;width:56px">Step Three (B)</div>
  <div class="note" style="left:268px;top:113px;width:163px;height:128px">
    <ul>
      <li>I move to position the child as the owner of their own learning.</li>
      <li>I give up control so the child can gain control.</li>
      <li>The child becomes an architect in their curriculum.</li>
      <li>The child becomes a collaborator in the how.</li>
      <li>I am more a learner than a teacher.</li>
      <li>I am a master of pedagogies.</li>
      <li>I reflect on my practice through the eyes of children.</li>
    </ul>
  </div>
  <div class="footer"><b>Mission Delivery</b><br>©2026 Calloway Brook Guidance - Principal<br>Certification Poimen: Shepherd</div>
  <div class="page">6</div>
</section>

<!-- Slide 7: step four -->
<section class="slide" style="left:27px;top:903px">
  <div class="brand-name">Calloway Brook</div>
  <div class="motto">For Jesus; Through Mission; With Children</div>
  <div class="tag step-tag" style="top:76px">Learning Journey</div>
  <div class="heading step-title" style="left:17px;top:93px">Step Four</div>
  <div class="card" style="left:14px;top:120px;width:250px;height:92px;display:flex;gap:12px">
    <ul style="flex:1">
      <li>I am comfortable both in making the child owner and in taking on leadership roles with colleagues.</li>
      <li>I want and work to ensure that every child to succeed.</li>
      <li>I see myself as a learner.</li>
      <li>I am a master of metacognition.</li>
    </ul>
    <ul style="flex:1.05">
      <li>I want and work to ensure that every one of my colleagues to succeed.</li>
      <li>I am a master of several pedagogies.</li>
      <li>I reflect on my practice with my children / teens.</li>
      <li>Children come to and stay at the school because I am there.</li>
    </ul>
  </div>
  <div class="placeholder" role="img" aria-label="Cartoon illustration of a teacher showing an apple card to three children, with a red heart and a blue thought cloud"
       style="left:273px;top:49px;width:169px;height:160px;border-radius:14px;background:linear-gradient(170deg,#dcecf8 0%,#f2c1b0 40%,#e25a4a 60%,#6aa6dc 85%,#f3f3f3 100%)"></div>
  <div class="footer"><b>Mission Delivery</b><br>©2026 Calloway Brook Guidance - Principal<br>Certification Poimen: Shepherd</div>
  <div class="page">7</div>
</section>

</body>
</html>
```